Software company WebSite Design (enterprise level SW, Mobile apps, HW prototypes)

We need design for our new webpages. We got new logo and new business cards and we need webdesign which will be match with those two.
We are dealing with corporate level software development - enterprise level portals, development of optimalization SW, route planning optimalizations. For a few months we are developing mobile applications for companies.
IMPORTANT is to express the cutting edge technological company.

Target Market(s)

IT company customers

Industry/Entity Type

Business

Number of Pages Required

2 page

Requirements
Must have
• Project needs to have landing page and product detail page. Design needs to be created including full font and example images as there would be a real webpage. Design should be clean, modern and expressing hi-tech level of the company.
• Example of well designer web pages - www.quorvelt.com, www.brandissa.com - We like the font formatting and font designs (colors, placing, etc - its professional).
• Attached image contains screenshot from old web landing page. It contains basic sections of our business (Simulation Tools, Enterprise Intranet Systems, Hi-tech web presentations, Supporting Enterprise services - Optimalization and logistics monitoring)

```html
<!DOCTYPE html>
<html lang="en">
<head>
<meta charset="utf-8">
<title>Nexalo Solutions</title>
<link href="https://fonts.googleapis.com/css2?family=Raleway:wght@300;400;500;600&family=Open+Sans:wght@400;600&display=swap" rel="stylesheet">
<style>
:root{
  --orange:#f98a05;
  --ink:#222;
  --text:#555;
  --muted:#888;
  --light:#f5f5f5;
  --circle:#e9e9e9;
  --dark:#1c1c1c;
  --darker:#141414;
  --white:#fff;
}
*{margin:0;padding:0;box-sizing:border-box}
html,body{width:1200px;height:2344px;overflow:hidden}
body{position:relative;font-family:"Open Sans",sans-serif;color:var(--text);background:var(--white)}
.abs{position:absolute}
.heading{font-family:"Raleway",sans-serif;font-weight:400;color:var(--ink)}
.rule{position:absolute;height:2px;background:var(--orange);width:54px}
.btn{position:absolute;background:var(--orange);color:var(--white);border-radius:18px;font-size:12px;display:flex;align-items:center;justify-content:center}

/* hero */
.hero{position:absolute;left:0;top:0;width:1200px;height:569px;background:linear-gradient(100deg,#2b2d30 0%,#3a3c3f 45%,#2f3134 70%,#3c3e41 100%)}
.brand{left:86px;top:16px;display:flex;align-items:center;gap:12px;color:var(--white);font-family:"Raleway",sans-serif;font-weight:600;font-size:28px;letter-spacing:1px}
.brand .mark{width:36px;height:36px;border:3px solid var(--white)}
.nav{right:88px;top:23px;display:flex;gap:21px;font-size:11.5px;font-weight:600;color:var(--white);white-space:nowrap}
.nav .active{color:var(--orange);border-bottom:2px solid var(--orange);padding-bottom:6px}
.hero-title{left:0;width:1200px;top:228px;text-align:center;font-family:"Raleway",sans-serif;font-size:64px;font-weight:400;color:var(--white)}
.hero-text{left:290px;width:620px;top:302px;text-align:center;font-size:12px;line-height:22px;color:#ddd}
.pager{left:1130px;top:204px;width:36px;text-align:center;color:var(--white);font-size:14px;font-weight:600}
.pager div{height:40px;line-height:40px}
.pager .on{color:var(--orange);font-size:18px}

/* provide */
.provide-title{left:0;width:1200px;top:596px;text-align:center;font-size:28px}
.service-circle{width:92px;height:92px;border-radius:50%;background:var(--circle);display:flex;align-items:center;justify-content:center}
.service-circle.on{background:var(--orange)}
.track{left:339px;top:815px;width:520px;height:2px;background:#ddd}
.dot{width:14px;height:14px;border-radius:50%;background:#bbb}
.dot.on{background:var(--orange)}
.service-label{width:200px;text-align:center;font-size:11px;color:var(--text);line-height:18px;top:840px}

/* presentations */
.presentations{left:0;top:906px;width:1200px;height:341px;background:var(--light)}
.photo{box-shadow:0 2px 10px rgba(0,0,0,.2);border:6px solid var(--white)}
.section-title{font-size:28px}
.body-copy{font-size:12.5px;line-height:23px;color:var(--text)}

/* ship */
.ship-title{left:132px;width:410px;top:1326px;text-align:right;font-size:27px;line-height:33px}
.ship-title em{font-style:normal;color:var(--orange)}
.ship-list{right:658px;top:1426px;text-align:right;font-size:13px;color:var(--text)}
.ship-list li{list-style:none;height:31px;display:flex;align-items:center;justify-content:flex-end;gap:14px;white-space:nowrap}

/* testimonials */
.quote{width:314px;height:147px;border:1px solid #ddd;background:var(--white);padding:26px 30px}
.quote h4{font-size:14px;font-weight:600;color:#333;margin-bottom:6px}
.quote p{font-size:11.5px;line-height:18px;color:var(--text)}
.stars{color:#f4c20d;font-size:13px;letter-spacing:2px;margin-top:6px}
.avatar{width:62px;height:62px;border-radius:50%;border:3px solid var(--white);box-shadow:0 1px 4px rgba(0,0,0,.3)}

/* stats */
.stats{left:0;top:1900px;width:1200px;height:147px;background:var(--orange)}
.stat{top:1922px;width:220px;color:var(--white);text-align:center;white-space:nowrap}
.stat .num{font-size:46px;line-height:56px}
.stat .line{width:110px;height:1px;background:rgba(255,255,255,.6);margin:8px auto 10px}
.stat .label{font-size:15px;font-weight:600}

/* footer */
.footer{left:0;top:2047px;width:1200px;height:255px;background:var(--dark)}
.foot-head{font-size:17px;font-weight:600;color:var(--white);top:2076px}
.foot-rule{top:2108px;height:1px;width:80px;background:#555}
.foot-text{font-size:12px;line-height:22px;color:#ddd}
.foot-links li{list-style:none;font-size:11.5px;line-height:22.5px;color:#ddd}
.contact-row{display:flex;align-items:center;gap:12px;font-size:11.5px;color:#ddd;white-space:nowrap}
.round-icon{width:28px;height:28px;border-radius:50%;background:var(--orange);display:flex;align-items:center;justify-content:center}
.email-field{left:878px;top:2125px;width:232px;height:36px;border:1px solid #aaa;color:var(--white);font-size:12px;padding:9px 10px}
.copyright{left:0;top:2302px;width:1200px;height:42px;background:var(--darker);border-top:1px solid #2e2e2e;color:#ddd;font-size:11.5px;text-align:center;line-height:42px}
</style>
</head>
<body>

<header class="hero" role="img" aria-label="Dimmed photo of a team working in a bright office"></header>
<div class="abs brand"><span class="mark"></span>Nexalo</div>
<nav class="abs nav">
  <span class="active">HOME</span><span>PRODUCT</span><span>CUSTOMERS</span><span>PRICING</span><span>DEVELOPERS</span><span>SUPPORT</span><span>RESOURCES</span>
  <svg width="20" height="14" viewBox="0 0 20 14"><path d="M4 1h16M0 7h20M4 13h16" stroke="#fff" stroke-width="2"/></svg>
</nav>
<h1 class="abs hero-title">Welcome To Nexalo</h1>
<p class="abs hero-text">Lorem Ipsum is simply dummy text of the printing and typesetting industry. Lorem Ipsum has been the industry's standard dummy text ever since the 1500s</p>
<div class="btn" style="left:547px;top:366px;width:111px;height:34px">Read More</div>
<div class="abs pager">
  <div>&#8593;</div><div>01</div><div class="on">02</div><div>03</div><div>&#8595;</div>
</div>

<!-- what we provide -->
<h2 class="abs heading provide-title">What We Provide</h2>
<span class="rule" style="left:573px;top:640px"></span>

<div class="abs service-circle" style="left:293px;top:682px">
  <svg width="38" height="30" viewBox="0 0 38 30" fill="none" stroke="#555" stroke-width="2"><rect x="7" y="4" width="24" height="16"/><path d="M2 24h34v2H2z"/></svg>
</div>
<div class="abs service-circle" style="left:468px;top:682px">
  <svg width="34" height="30" viewBox="0 0 34 30" fill="none" stroke="#555" stroke-width="2"><path d="M2 4h5l4 15h16l3-11H9"/><circle cx="13" cy="25" r="2"/><circle cx="25" cy="25" r="2"/></svg>
</div>
<div class="abs service-circle on" style="left:646px;top:682px">
  <svg width="40" height="32" viewBox="0 0 40 32" fill="none" stroke="#fff" stroke-width="2.2"><path d="M10 24a7 7 0 0 1 0-14 9 9 0 0 1 17-2 7 7 0 0 1 3 16z"/><path d="M20 14v12M16 22l4 4 4-4"/></svg>
</div>
<div class="abs service-circle" style="left:808px;top:682px">
  <svg width="38" height="30" viewBox="0 0 38 30" fill="none" stroke="#555" stroke-width="2"><rect x="5" y="3" width="28" height="18"/><path d="M2 25h34M15 9l-3 3 3 3M23 9l3 3-3 3"/></svg>
</div>

<div class="abs track"></div>
<div class="abs dot" style="left:332px;top:809px"></div>
<div class="abs dot" style="left:507px;top:809px"></div>
<div class="abs dot on" style="left:685px;top:809px"></div>
<div class="abs dot" style="left:851px;top:809px"></div>
<div class="abs service-label" style="left:239px">ENTERPRISE PORTAL</div>
<div class="abs service-label" style="left:414px">OPTIMIZATION SW</div>
<div class="abs service-label" style="left:592px">ROUTE PLANING<br>OPTIMALIZATION</div>
<div class="abs service-label" style="left:758px">MOBILE APPLICATION</div>

<!-- presentations -->
<section class="abs presentations"></section>
<div class="abs photo" role="img" aria-label="Photo of a modern wooden building facade against a blue sky" style="left:112px;top:955px;width:200px;height:192px;background:linear-gradient(160deg,#7da3c8 0%,#8d8a80 45%,#9b6a42 100%)"></div>
<div class="abs" style="left:197px;top:978px;width:253px;height:219px;border:3px solid var(--orange)"></div>
<div class="abs photo" role="img" aria-label="Photo of a man with a laptop sitting on a sofa" style="left:206px;top:988px;width:262px;height:196px;background:linear-gradient(135deg,#c9c4bb 0%,#6e6a66 55%,#3d4350 100%)"></div>
<h2 class="abs heading section-title" style="left:512px;top:956px">Hi-tech Web Presentations</h2>
<span class="rule" style="left:512px;top:996px"></span>
<p class="abs body-copy" style="left:512px;top:1016px;width:592px">Lorem Ipsum is simply dummy text of the printing and typesetting industry. Lorem Ipsum has been the industry's standard dummy text ever since the 1500s, when an unknown printer took a galley of type and scrambled it to make a type specimen book. It has survived not only five centuries, but also the leap into electronic typesetting, remaining essentially unchanged. It was popularised in the 1960s</p>
<div class="btn" style="left:506px;top:1148px;width:111px;height:35px">Read More</div>

<!-- ship -->
<h2 class="abs heading ship-title">Ship <em>better apps</em> faster with For Any Network</h2>
<span class="rule" style="left:488px;top:1402px"></span>
<ul class="abs ship-list">
  <li>Contrary to popular belief<svg width="17" height="17" viewBox="0 0 17 17"><circle cx="8.5" cy="8.5" r="8.5" fill="#f98a05"/><path d="M5 9l2.5 2.5L12 6.5" stroke="#fff" stroke-width="1.8" fill="none"/></svg></li>
  <li>Lorem Ipsum is simply dummy text<svg width="17" height="17" viewBox="0 0 17 17"><circle cx="8.5" cy="8.5" r="8.5" fill="#f98a05"/><path d="M5 9l2.5 2.5L12 6.5" stroke="#fff" stroke-width="1.8" fill="none"/></svg></li>
  <li>It is a long established fact that a reader<svg width="17" height="17" viewBox="0 0 17 17"><circle cx="8.5" cy="8.5" r="8.5" fill="#f98a05"/><path d="M5 9l2.5 2.5L12 6.5" stroke="#fff" stroke-width="1.8" fill="none"/></svg></li>
</ul>
<div class="abs" role="img" aria-label="Photo of a laptop screen showing analytics charts" style="left:572px;top:1306px;width:537px;height:269px;background:linear-gradient(110deg,#f1efec 0%,#d9dde3 40%,#5a6270 75%,#2e333b 100%);box-shadow:0 6px 14px rgba(0,0,0,.25)"></div>

<!-- testimonials -->
<h2 class="abs heading section-title" style="left:0;width:1200px;top:1616px;text-align:center">Client Testimonial</h2>
<span class="rule" style="left:573px;top:1660px"></span>

<div class="abs quote" style="left:91px;top:1689px"><h4>JOHN SAYS...</h4><p>Lorem ipsum dolor sit amet, consectetuer adipiscing elit. Aenean commodo ligula eget dolor. Aenean massa.</p><div class="stars">&#9733;&#9733;&#9733;&#9733;&#9733;</div></div>
<div class="abs quote" style="left:445px;top:1689px"><h4>CARL SAYS...</h4><p>Lorem ipsum dolor sit amet, consectetuer adipiscing elit. Aenean commodo ligula eget dolor. Aenean massa.</p><div class="stars">&#9733;&#9733;&#9733;&#9733;&#9733;</div></div>
<div class="abs quote" style="left:800px;top:1689px"><h4>MICHAEL SAYS...</h4><p>Lorem ipsum dolor sit amet, consectetuer adipiscing elit. Aenean commodo ligula eget dolor. Aenean massa.</p><div class="stars">&#9733;&#9733;&#9733;&#9733;&#9733;</div></div>
<div class="abs avatar" role="img" aria-label="Portrait of John" style="left:325px;top:1661px;background:#8a7a6a"></div>
<div class="abs avatar" role="img" aria-label="Portrait of Carl" style="left:682px;top:1661px;background:#d8c2a8"></div>
<div class="abs avatar" role="img" aria-label="Portrait of Michael" style="left:1030px;top:1661px;background:#4a4440"></div>
<div class="abs dot" style="left:583px;top:1859px;width:9px;height:9px;background:#ccc"></div>
<div class="abs dot on" style="left:598px;top:1859px;width:9px;height:9px"></div>
<div class="abs dot" style="left:613px;top:1859px;width:9px;height:9px;background:#ccc"></div>

<!-- stats -->
<section class="abs stats"></section>
<div class="abs stat" style="left:60px"><div class="num">2.5 M+</div><div class="line"></div><div class="label">DEVELOPERS</div></div>
<div class="abs stat" style="left:359px"><div class="num">130 K</div><div class="line"></div><div class="label">CUSTOMERS</div></div>
<div class="abs stat" style="left:660px"><div class="num">20 K</div><div class="line"></div><div class="label">CLIENTS</div></div>
<div class="abs stat" style="left:945px"><div class="num">300+</div><div class="line"></div><div class="label">AWARDS</div></div>

<!-- footer -->
<footer class="abs footer"></footer>
<div class="abs foot-head" style="left:92px">ABOUT US</div>
<div class="abs foot-rule" style="left:92px"></div>
<p class="abs foot-text" style="left:92px;top:2120px;width:245px">Etiam sit amet orci eget eros faucibus tincidunt. Duis leo. Sed fringilla mauris sit amet nibh. Donec sodales sagittis magna.</p>
<div class="abs contact-row" style="left:92px;top:2192px"><span class="round-icon"><svg width="10" height="14" viewBox="0 0 10 14"><rect x="1" y="1" width="8" height="12" rx="1.5" fill="none" stroke="#fff" stroke-width="1.5"/></svg></span>Call Us : +123-456-7890</div>
<div class="abs contact-row" style="left:92px;top:2226px"><span class="round-icon"><svg width="12" height="9" viewBox="0 0 12 9"><rect x="0.5" y="0.5" width="11" height="8" fill="none" stroke="#fff"/><path d="M.5.5l5.5 4.5 5.5-4.5" stroke="#fff" fill="none"/></svg></span>info@domain.com</div>

<div class="abs foot-head" style="left:417px">RESOURCES</div>
<div class="abs foot-rule" style="left:417px"></div>
<ul class="abs foot-links" style="left:417px;top:2120px"><li>Demos</li><li>Documentation</li><li>Release History</li><li>Forums</li><li>Blogs</li><li>Developer Network</li><li>Events</li></ul>

<div class="abs foot-head" style="left:645px">CONTACT</div>
<div class="abs foot-rule" style="left:645px"></div>
<div class="abs contact-row" style="left:645px;top:2130px;align-items:flex-start"><svg width="12" height="16" viewBox="0 0 12 16"><path d="M6 0a6 6 0 0 1 6 6c0 4-6 10-6 10S0 10 0 6a6 6 0 0 1 6-6z" fill="#aaa"/><circle cx="6" cy="6" r="2" fill="#1c1c1c"/></svg><span style="line-height:19px">Halvern Strasse 42b<br>10920 Berlin</span></div>
<div class="abs contact-row" style="left:645px;top:2186px"><svg width="14" height="14" viewBox="0 0 14 14"><path d="M3 0l3 3-2 2a8 8 0 0 0 5 5l2-2 3 3-2 3C6 14 0 8 0 3z" fill="#aaa"/></svg>Phone: 123-456-7890</div>
<div class="abs contact-row" style="left:645px;top:2223px"><svg width="14" height="10" viewBox="0 0 14 10"><rect x=".5" y=".5" width="13" height="9" fill="none" stroke="#aaa"/><path d="M.5.5L7 5.5 13.5.5" stroke="#aaa" fill="none"/></svg>info@domain.com</div>

<div class="abs foot-head" style="left:878px">NEWSLETTER</div>
<div class="abs foot-rule" style="left:878px"></div>
<div class="abs email-field">Email</div>
<div class="btn" style="left:875px;top:2175px;width:102px;height:30px;font-size:11px">SEND</div>

<div class="abs copyright">Copyright 2016. All Right Reserved</div>

</body>
</html>
```